Sales Flyer Design

Create a Flyer front and back that highlights the different things we do
We do Addition, basements, kitchens, bathrooms, concrete, siding, Roofing.

We want to highlight that we are licensed Electrical Contractor and Plumbers.
Use our Logo attached keeping color scheme mainly our company colors. We are looking for an attention grabbing but easy read for homeowners.

```html
<!DOCTYPE html>
<html lang="en">
<head>
<meta charset="utf-8">
<title>Holloway Remodeling &amp; Restoration — Flyer Front and Back</title>
<link href="https://fonts.googleapis.com/css2?family=Barlow+Condensed:wght@500;600;700&family=Barlow:ital,wght@0,400;0,500;0,600;1,400&display=swap" rel="stylesheet">
<style>
:root{
  --orange:#d8541a;
  --orange-bright:#e86a22;
  --ink:#141414;
  --charcoal:#1e1e1e;
  --white:#ffffff;
  --paper:#fafafa;
  --backdrop:#e9e9ea;
  --muted:#2b2b2b;
}
*{box-sizing:border-box;margin:0;padding:0}
html,body{width:1200px;height:800px;overflow:hidden;background:var(--backdrop)}
body{position:relative;font-family:"Barlow",Arial,sans-serif;color:var(--ink)}
.head{font-family:"Barlow Condensed","Arial Narrow",sans-serif;font-weight:700;text-transform:uppercase;line-height:1}

.flyer{position:absolute;top:66px;width:501px;height:668px;overflow:hidden;box-shadow:0 10px 24px rgba(0,0,0,.22)}
.flyer--front{left:75px;background:var(--charcoal)}
.flyer--back{left:624px;background:var(--paper)}

/* front */
.front-photo{position:absolute;inset:0;background:linear-gradient(180deg,#2a2a2a 0%,#4a4643 45%,#3a3633 70%,#2a2826 100%)}
.front-title{position:absolute;top:28px;left:0;width:100%;text-align:center;font-size:49px;color:var(--white);letter-spacing:.5px}
.front-title span{display:block;color:var(--orange-bright);margin-top:4px}
.front-sub{position:absolute;top:140px;left:0;width:100%;text-align:center;font-family:"Barlow Condensed",sans-serif;font-weight:600;font-size:20px;color:var(--white);line-height:1.3;text-transform:uppercase}

.specialties{position:absolute;left:0;top:290px;width:304px;height:292px;background:rgba(20,20,20,.88);padding:18px 0 0 40px}
.specialties h2{font-size:33px;color:var(--white);margin-bottom:10px}
.specialties ul{list-style:none}
.specialties li{display:flex;align-items:center;gap:12px;color:var(--white);font-size:23px;font-weight:500;height:33.5px;white-space:nowrap}
.specialties svg{width:18px;height:18px;flex:none}

.license-tag{position:absolute;left:316px;width:185px;background:var(--orange);display:flex;align-items:center;gap:12px;padding:0 10px 0 16px}
.license-tag svg{width:36px;height:36px;flex:none}
.license-tag p{font-size:23px;color:var(--white);line-height:.95}
.license-tag--electric{top:295px;height:80px}
.license-tag--plumb{top:390px;height:81px}

.front-footer{position:absolute;left:0;bottom:0;width:100%;height:125px;background:var(--ink)}
.front-footer .cta{position:absolute;left:0;top:0;width:323px;height:100%;background:var(--orange);clip-path:polygon(0 0,100% 0,85.5% 100%,0 100%)}
.cta h3{position:absolute;left:50px;top:18px;font-size:30px;color:var(--white);line-height:1.05;text-align:center}
.cta .contact{position:absolute;left:52px;font-size:16px;color:var(--white);display:flex;align-items:center;gap:8px}
.cta .contact svg{width:14px;height:14px}
.cta .contact--mail{top:85px}
.cta .contact--web{top:106px}
.brand{position:absolute;right:14px;top:32px;width:180px;text-align:center;color:var(--white)}
.brand .name{font-family:"Barlow Condensed",sans-serif;font-weight:700;font-size:36px;letter-spacing:1px;display:flex;align-items:center;justify-content:center;gap:8px}
.brand .name i{display:inline-block;width:12px;height:12px;background:var(--orange)}
.brand .tag{font-family:"Barlow Condensed",sans-serif;font-weight:500;font-size:12px;letter-spacing:1px;margin-top:10px;text-transform:uppercase}

/* back */
.back-title{position:absolute;top:30px;left:0;width:100%;text-align:center;font-size:45px;color:var(--orange)}
.trust{position:absolute;top:87px;width:150px;text-align:center}
.trust svg{width:44px;height:44px;display:block;margin:0 auto 10px}
.trust h3{font-size:20px;color:var(--ink);line-height:1.05}
.trust p{font-size:12.5px;line-height:17px;margin-top:8px;color:var(--muted)}
.trust--license{left:26px}
.trust--service{left:176px}
.trust--warranty{left:330px;width:160px}

.shot{position:absolute;top:274px;width:222px;height:181px}
.shot--before{left:26px}
.shot--after{left:258px}
.shot .fill{position:absolute;inset:0;background:linear-gradient(160deg,#f2efea 0%,#dcd6cd 55%,#8a6a4d 100%)}
.shot .label{position:absolute;left:0;bottom:0;width:95px;height:32px;background:var(--ink);color:var(--white);font-size:21px;display:flex;align-items:center;padding-left:16px}

.quote{position:absolute;top:465px;left:90px;width:321px;text-align:center;font-style:italic;font-size:16px;line-height:22px;color:var(--ink)}

.back-footer{position:absolute;left:0;bottom:0;width:100%;height:128px;background:var(--ink);color:var(--white)}
.back-footer .ask{position:absolute;left:30px;top:18px;font-size:32px;line-height:1.05}
.back-footer .call{position:absolute;left:292px;top:28px;font-size:29px}
.back-footer .phone{position:absolute;left:292px;top:65px;font-size:31px}
.back-footer .web{position:absolute;left:293px;top:104px;font-size:16px;font-weight:500}
</style>
</head>
<body>

<section class="flyer flyer--front">
  <div class="front-photo" role="img" aria-label="Dim photo of a finished modern kitchen interior"></div>

  <h1 class="head front-title">Transform Your Home<span>With Confidence!</span></h1>
  <p class="front-sub">Licensed Electrical &amp; Plumbing Contractor<br>Fully Insured | Trusted by Homeowners</p>

  <div class="specialties">
    <h2 class="head">We Specialize In:</h2>
    <ul>
      <li><svg viewBox="0 0 20 20"><path d="M2 11l5 5L18 4" fill="none" stroke="#e86a22" stroke-width="3.5" stroke-linecap="round" stroke-linejoin="round"/></svg>Home Additions</li>
      <li><svg viewBox="0 0 20 20"><path d="M2 11l5 5L18 4" fill="none" stroke="#e86a22" stroke-width="3.5" stroke-linecap="round" stroke-linejoin="round"/></svg>Kitchens &amp; Bathrooms</li>
      <li><svg viewBox="0 0 20 20"><path d="M2 11l5 5L18 4" fill="none" stroke="#e86a22" stroke-width="3.5" stroke-linecap="round" stroke-linejoin="round"/></svg>Finished Basements</li>
      <li><svg viewBox="0 0 20 20"><path d="M2 11l5 5L18 4" fill="none" stroke="#e86a22" stroke-width="3.5" stroke-linecap="round" stroke-linejoin="round"/></svg>Roofing &amp; Siding</li>
      <li><svg viewBox="0 0 20 20"><path d="M2 11l5 5L18 4" fill="none" stroke="#e86a22" stroke-width="3.5" stroke-linecap="round" stroke-linejoin="round"/></svg>Concrete Work</li>
    </ul>
  </div>

  <div class="license-tag license-tag--electric">
    <svg viewBox="0 0 40 40"><path d="M28 4a8 8 0 0 0-7 11L6 30a3 3 0 0 0 4 4l15-15a8 8 0 0 0 11-7l-5 3-4-2-1-4z" fill="#fff"/></svg>
    <p class="head">Licensed<br>Electrical<br>Contractor</p>
  </div>
  <div class="license-tag license-tag--plumb">
    <svg viewBox="0 0 40 40"><path d="M4 14h20v-4h-6V7h14v3h-6v4h4a6 6 0 0 1 6 6v4h-6v-3H4z" fill="#fff"/><path d="M31 30c0 3-2 4-3 4s-3-1-3-4l3-4z" fill="#fff"/></svg>
    <p class="head">Licensed<br>Plumbing<br>Services</p>
  </div>

  <footer class="front-footer">
    <div class="cta">
      <h3 class="head">Call Us Today for<br>a Free Estimate!</h3>
      <p class="contact contact--mail"><svg viewBox="0 0 16 16"><rect x="1" y="3" width="14" height="10" fill="none" stroke="#fff" stroke-width="1.5"/><path d="M1 3l7 6 7-6" fill="none" stroke="#fff" stroke-width="1.5"/></svg>info@hollowayremodel.com</p>
      <p class="contact contact--web"><svg viewBox="0 0 16 16"><circle cx="8" cy="8" r="6.5" fill="none" stroke="#fff" stroke-width="1.5"/><path d="M1.5 8h13M8 1.5c3 3 3 10 0 13M8 1.5c-3 3-3 10 0 13" fill="none" stroke="#fff" stroke-width="1.2"/></svg>www.hollowayremodel.com</p>
    </div>
    <div class="brand">
      <p class="name"><i></i>HOLLOWAY</p>
      <p class="tag">Remodeling &amp; Restoration</p>
    </div>
  </footer>
</section>

<section class="flyer flyer--back">
  <h2 class="head back-title">Why Homeowners Trust Us</h2>

  <div class="trust trust--license">
    <svg viewBox="0 0 48 48"><path d="M24 3l18 6v13c0 12-8 20-18 23C14 42 6 34 6 22V9z" fill="#141414"/><path d="M15 24l6 6 12-12" fill="none" stroke="#fff" stroke-width="4" stroke-linecap="round" stroke-linejoin="round"/></svg>
    <h3 class="head">Licensed &amp;<br>Insured</h3>
    <p>We follow all codes<br>and regulations –<br>your home is in safe<br>hands.</p>
  </div>
  <div class="trust trust--service">
    <svg viewBox="0 0 48 48"><path d="M6 6h28v10H22v8h-6v-8H6z" fill="#141414"/><path d="M34 8h4a6 6 0 0 1 0 12h-2v-4h2a2 2 0 0 0 0-4h-4z" fill="#141414"/><path d="M16 26h6v6h6v6h-6v6h-6v-6h-6v-6h6z" fill="#141414"/></svg>
    <h3 class="head">All-in-One<br>Service</h3>
    <p>From foundation to<br>finish – electrical, plumbing,<br>remodeling under one<br>roof.</p>
  </div>
  <div class="trust trust--warranty">
    <svg viewBox="0 0 48 48"><path d="M24 3l18 6v13c0 12-8 20-18 23C14 42 6 34 6 22V9z" fill="#141414"/><path d="M14 25l10-9 10 9h-3v8h-5v-5h-4v5h-5v-8z" fill="#fff"/></svg>
    <h3 class="head">Warranty &amp;<br>Clean Worksites</h3>
    <p>We respect your home<br>and back our work<br>with strong warranties.</p>
  </div>

  <div class="shot shot--before">
    <div class="fill" role="img" aria-label="Kitchen before renovation with white cabinets and range"></div>
    <span class="label head">Before</span>
  </div>
  <div class="shot shot--after">
    <div class="fill" role="img" aria-label="Kitchen after renovation with new cabinets, microwave and wood floor"></div>
    <span class="label head">After</span>
  </div>

  <p class="quote">“They renovated our basement beautifully and fixed our old wiring. Reliable, neat, and professional.”</p>

  <footer class="back-footer">
    <p class="head ask">Ready to Start<br>Your Dream<br>Project?</p>
    <p class="head call">Call Today:</p>
    <p class="head phone">555-204-7781</p>
    <p class="web">www.hollowayremodel.com</p>
  </footer>
</section>

</body>
</html>
```